TOASTED COCONUT CHIPS

My company is a food company specialised in coconut products. The subject project is to design the package bag and respective simple shipping case for toasted coconut chips for two flavors: one is original and the other is cinnamon. I also need a logo design for the brand "pimlo".

I would like the bag looks simple, classy and attractive. Or the other way that it could look cute and fun.

The design will include two flavors: original/sea salt and cinnamon
The design need to be fit in 40g pouch bag and 20g bag.
Need the design of the bag and subsequently the shipping case.

Target Market(s)

age 8 to 40
sell in cafeteria and vending machine

Industry/Entity Type

It Company

Logo Text

simple and direct

Requirements
Must have
• golden coconut chips picture on the front side.
• the bag should looks clean but attractive.
• Otherwise, it has to be very colourful to attract eye balls.
• I need the design can be fit in a 40g pouch and 20g cutie size bag
Should not have
• Should not look Asian food.

```html
<!DOCTYPE html>
<html lang="en">
<head>
<meta charset="utf-8">
<title>pimlo roasted crispy coconut chips</title>
<link href="https://fonts.googleapis.com/css2?family=Open+Sans:wght@300;400;700&display=swap" rel="stylesheet">
<style>
  :root {
    --bg: #ffffff;
    --seal: #d4d4d4;
    --window: #e9e9e9;
    --window-shine: #f6f6f6;
    --band: #050505;
    --brand-green: #6fbf2a;
    --subtitle: #f2f2f2;
    --claims-text: #7a1414;
    --claims-panel: rgba(255, 255, 255, 0.72);
    --cinnamon-band: #6b0808;
    --cinnamon-label: #d2a472;
    --salted-band: #a37b55;
    --salted-label: #f6efe6;
  }
  * { box-sizing: border-box; margin: 0; padding: 0; }
  html, body { width: 1200px; height: 889px; overflow: hidden; background: var(--bg); }
  body { position: relative; font-family: "Open Sans", Arial, sans-serif; }

  .pouch {
    position: absolute; top: 66px; width: 510px; height: 780px;
    background: var(--seal); border-radius: 14px 14px 6px 6px;
  }
  .pouch--cinnamon { left: 92px; }
  .pouch--salted { left: 616px; }

  .pouch__window {
    position: absolute; left: 44px; right: 44px; top: 34px; height: 116px;
    background: linear-gradient(180deg, var(--window-shine), var(--window));
    border-radius: 14px 14px 0 0;
  }
  .pouch__zip {
    position: absolute; left: 44px; right: 44px; top: 100px; height: 10px;
    background: rgba(255,255,255,0.7);
  }
  .pouch__band {
    position: absolute; left: 8px; right: 8px; top: 150px; height: 206px;
    background: var(--band);
  }
  .brand {
    position: absolute; left: 0; right: 0; top: 22px;
    display: flex; align-items: center; justify-content: center; gap: 16px;
  }
  .brand__name {
    font-family: "Open Sans", Arial, sans-serif; font-weight: 700;
    font-size: 104px; line-height: 1; color: var(--brand-green); letter-spacing: -2px;
  }
  .brand__dot { width: 60px; height: 60px; border-radius: 50%; background: var(--brand-green); }
  .pouch__subtitle {
    position: absolute; left: 0; right: 0; top: 162px; text-align: center;
    font-weight: 300; font-size: 18px; color: var(--subtitle); letter-spacing: -0.3px;
  }

  .pouch__photo {
    position: absolute; left: 44px; right: 8px; top: 356px; height: 330px;
  }
  .pouch--cinnamon .pouch__photo {
    background: radial-gradient(ellipse at 60% 40%, #f3e2c8 0%, #dcb88a 45%, #b98a5a 75%, #cfd6d6 100%);
  }
  .pouch--salted .pouch__photo {
    background: radial-gradient(ellipse at 62% 38%, #f4dca4 0%, #e6c27e 40%, #a48a6a 72%, #6e5f52 100%);
  }

  .claims {
    position: absolute; left: 58px; top: 440px; width: 138px; height: 158px;
    background: var(--claims-panel); padding: 12px 0 0 14px;
    list-style: none; color: var(--claims-text); font-size: 9px; line-height: 11.3px;
  }

  .pouch__flavour {
    position: absolute; left: 44px; right: 8px; top: 686px; height: 86px;
    border-radius: 0 0 10px 10px;
    display: flex; align-items: center; justify-content: center;
    font-weight: 300; font-size: 38px; letter-spacing: 0.5px;
  }
  .pouch--cinnamon .pouch__flavour { background: var(--cinnamon-band); color: var(--cinnamon-label); }
  .pouch--salted .pouch__flavour { background: var(--salted-band); color: var(--salted-label); }
</style>
</head>
<body>

<section class="pouch pouch--cinnamon">
  <div class="pouch__window"></div>
  <div class="pouch__zip"></div>
  <header class="pouch__band">
    <div class="brand"><span class="brand__name">pimlo</span><span class="brand__dot"></span></div>
    <p class="pouch__subtitle">ROASTED CRISPY COCONUT CHIPS</p>
  </header>
  <div class="pouch__photo" role="img" aria-label="Photo of golden roasted coconut chips dusted with cinnamon in a glass jar"></div>
  <ul class="claims">
    <li>All Natural ingredients</li><li>Not fried</li><li>Vegan</li><li>Gluten Free</li><li>Vegan</li>
    <li>Dairy Free</li><li>No Cholesterol</li><li>No Preservative</li><li>No Artifical Color</li>
    <li>No Artificial Flavouring</li><li>Good Source of Fiber</li>
  </ul>
  <div class="pouch__flavour">cinnamon</div>
</section>

<section class="pouch pouch--salted">
  <div class="pouch__window"></div>
  <div class="pouch__zip"></div>
  <header class="pouch__band">
    <div class="brand"><span class="brand__name">pimlo</span><span class="brand__dot"></span></div>
    <p class="pouch__subtitle">ROASTED CRISPY COCONUT CHIPS</p>
  </header>
  <div class="pouch__photo" role="img" aria-label="Photo of golden salted coconut chips in a white bowl"></div>
  <ul class="claims">
    <li>All Natural ingredients</li><li>Not fried</li><li>Vegan</li><li>Gluten Free</li><li>Vegan</li>
    <li>Dairy Free</li><li>No Cholesterol</li><li>No Preservative</li><li>No Artifical Color</li>
    <li>No Artificial Flavouring</li><li>Good Source of Fiber</li>
  </ul>
  <div class="pouch__flavour">original/ salted</div>
</section>

</body>
</html>
```